Upgrade Wordpress Website

We have an existing website www.bramblefinch.org.au - we require improved shop, improved donation visibility and interactive forms for sponsorship

```html
<!DOCTYPE html>
<html lang="en">
<head>
<meta charset="utf-8">
<title>Bramblefinch Equine Sanctuary</title>
<link href="https://fonts.googleapis.com/css2?family=Merienda:wght@400;700&family=Playfair+Display:ital@1&family=Poppins:wght@500;600&family=Roboto:wght@400;500;700&display=swap" rel="stylesheet">
<style>
:root{
  --orange:#f7923a;
  --orange-deep:#f07e22;
  --red:#e0111f;
  --ink:#222;
  --grey:#555;
  --white:#fff;
}
*{box-sizing:border-box;margin:0;padding:0}
html,body{width:1200px;height:3317px;overflow:hidden;background:var(--white);font-family:'Roboto',sans-serif;color:var(--ink)}
.page{position:relative;width:1200px;height:3317px}
.abs{position:absolute}
.script{font-family:'Merienda',cursive}
.kicker{font-family:'Playfair Display',serif;font-style:italic;color:var(--red);font-size:17px}

/* header */
.topbar{left:0;top:0;width:1200px;height:57px;border-top:3px solid var(--red);background:var(--white)}
.navbar{left:0;top:57px;width:1200px;height:61px;background:var(--orange)}
.brand-box{left:150px;top:0;width:170px;height:100px;background:var(--white);display:flex;align-items:center;justify-content:center;gap:7px;box-shadow:0 2px 6px rgba(0,0,0,.12)}
.brand-box .mark{width:22px;height:22px;background:var(--orange)}
.brand-box .name{font-weight:500;font-size:18px;color:var(--red);line-height:1.1}
.phone{left:688px;top:21px;font-size:13px;font-weight:500;display:flex;align-items:center;gap:5px}
.icon-btn{width:31px;height:31px;border-radius:50%;background:var(--red);top:15px;display:flex;align-items:center;justify-content:center}
.badge{left:896px;top:13px;width:13px;height:13px;border-radius:50%;background:#f0c419;font-size:9px;text-align:center;line-height:13px;color:var(--ink)}
.donate-top{left:927px;top:10px;width:122px;height:39px;background:var(--red);color:var(--white);font-size:11px;font-weight:700;display:flex;align-items:center;justify-content:center}
.nav{left:362px;top:76px;display:flex;gap:16px;font-family:'Merienda',cursive;font-size:10px;color:var(--white);font-style:italic;align-items:center}
.nav .active{background:var(--white);color:var(--red);padding:4px 10px}

/* hero */
.hero{left:0;top:118px;width:1200px;height:488px;background:linear-gradient(180deg,#7c8f93 0%,#8b7458 45%,#6b7a3f 75%,#7b8a45 100%)}
.hero-title{left:0;top:232px;width:1200px;text-align:center;font-size:56px;color:var(--white);font-weight:700;letter-spacing:1px;line-height:72px}
.mission{left:208px;top:372px;width:784px;height:150px;background:rgba(60,60,60,.55);text-align:center;color:var(--white)}
.mission h3{font-family:'Merienda',cursive;font-weight:400;font-size:26px;margin-top:10px}
.mission p{font-size:13.5px;line-height:22px;margin:8px 48px 0;font-weight:500}
.btn-white{left:544px;top:505px;width:113px;height:33px;background:var(--white);color:var(--red);font-weight:700;font-size:13px;display:flex;align-items:center;justify-content:center}
.dot{left:54px;width:16px;height:16px;border-radius:50%;background:var(--white)}

/* about */
.about-photo{left:343px;top:671px;width:857px;height:464px;background:linear-gradient(120deg,#3f5a2a,#a67446 45%,#c89764 60%,#2c2a2a)}
.about-card{left:122px;top:741px;width:476px;height:321px;background:var(--white);border:1px solid #e2e2e2;padding:25px 27px}
.title-box{display:flex;align-items:center;border:2px solid var(--orange);height:66px;gap:12px}
.title-box .sq{width:38px;height:62px;background:var(--orange)}
.title-box span{font-family:'Merienda',cursive;font-weight:700;font-size:44px;color:#111}
.about-card p{font-size:14px;line-height:22.5px;color:var(--grey);margin-top:22px}
.btn-red{background:var(--red);color:var(--white);font-weight:700;font-size:12px;display:flex;align-items:center;justify-content:center}

/* services */
.services{left:0;top:1198px;width:1200px;height:622px;background:linear-gradient(135deg,#f39643,#ef8631 60%,#f39a4a)}
.service{width:268px;height:268px;top:1397px;border:2px solid var(--white);display:flex;align-items:center;justify-content:center;color:var(--white);font-size:20px;letter-spacing:.3px}

/* products */
.product{width:213px;height:294px;top:2034px;border:1px solid #e9a36b;background:var(--orange)}
.product .img{height:218px}
.product .label{font-family:'Poppins',sans-serif;font-weight:600;font-size:18.5px;color:var(--white);line-height:22px;padding:0 14px;height:76px;display:flex;align-items:center}

/* contact */
.touch{left:0;top:2430px;width:1200px;height:488px;background:linear-gradient(90deg,#ec1a3c 0%,#f4502c 55%,#f58a3c 100%)}
.touch-title{left:0;top:2468px;width:1218px;text-align:center;font-family:'Merienda',cursive;font-size:50px;line-height:66px;color:var(--white);font-weight:400}
.field{background:var(--white);height:41px;font-size:12.5px;color:#b5b5b5;font-weight:700;padding:12px 13px}
.donate-card{left:133px;top:2837px;width:934px;height:131px;background:var(--white);box-shadow:0 2px 12px rgba(0,0,0,.15)}
.donate-card .info{position:absolute;left:138px;top:28px;font-size:10.5px;line-height:22px}
.donate-card .info b{font-size:12px}
.donate-big{left:787px;top:2855px;width:229px;height:57px;background:var(--orange);border-radius:8px;color:var(--white);font-family:'Poppins',sans-serif;font-weight:600;font-size:30px;display:flex;align-items:center;justify-content:center}
.card-shape{top:2924px;width:50px;height:30px;border-radius:3px}

/* footer */
.foot-brand{left:520px;top:3030px;width:160px;display:flex;align-items:center;justify-content:center;gap:8px}
.foot-brand .name{font-weight:500;font-size:22px;color:var(--red)}
.foot-brand .mark{width:34px;height:34px;background:var(--orange)}
.foot-nav{left:0;top:3133px;width:1200px;text-align:center;font-family:'Merienda',cursive;font-weight:700;font-size:13px;color:#111}
.foot-nav i{font-style:normal;margin:0 12px}
.contact-item{top:3195px;display:flex;align-items:center;gap:12px}
.contact-item .ring{width:58px;height:58px;border-radius:50%;border:2px solid var(--red);display:flex;align-items:center;justify-content:center}
.contact-item .txt{font-size:13.5px;color:var(--grey);line-height:19px}
.contact-item .txt b{font-family:'Poppins',sans-serif;font-size:16px;color:#111;font-weight:600;display:block}
.copyright{left:0;top:3286px;width:1200px;text-align:center;font-size:13px;color:#333}
.rule{top:3296px;height:1px;background:#333}
.to-top{left:1112px;top:3247px;width:40px;height:40px;border-radius:50%;background:linear-gradient(#f05a28,var(--red));border:2px solid #f4a0a0;display:flex;align-items:center;justify-content:center}
</style>
</head>
<body>
<div class="page">

  <!-- header -->
  <div class="abs topbar"></div>
  <div class="abs navbar"></div>
  <div class="abs brand-box"><span class="name">Bramblefinch</span><span class="mark"></span></div>
  <div class="abs phone">
    <svg width="11" height="11" viewBox="0 0 24 24"><path d="M6.6 10.8a15 15 0 0 0 6.6 6.6l2.2-2.2c.3-.3.7-.4 1-.2 1.1.4 2.3.6 3.6.6.6 0 1 .4 1 1V20c0 .6-.4 1-1 1A17 17 0 0 1 3 4c0-.6.4-1 1-1h3.5c.6 0 1 .4 1 1 0 1.3.2 2.5.6 3.6.1.3 0 .7-.2 1z" fill="#222"/></svg>
    1-800-555-0142
  </div>
  <div class="abs icon-btn" style="left:830px">
    <svg width="14" height="14" viewBox="0 0 24 24"><circle cx="12" cy="7" r="5" fill="#fff"/><path d="M3 22c0-5 4-8 9-8s9 3 9 8z" fill="#fff"/></svg>
  </div>
  <div class="abs icon-btn" style="left:873px">
    <svg width="16" height="14" viewBox="0 0 24 20"><path d="M2 7h20l-2 11H4z M7 7l5-6 5 6" fill="#fff" stroke="#fff"/></svg>
  </div>
  <div class="abs badge">0</div>
  <div class="abs donate-top">DONATE NOW</div>
  <nav class="abs nav">
    <span class="active">HOME</span><span>HORSES FOR ADOPTION</span><span>FOR SPONSORSHIP</span><span>SHOP</span><span>LEASE</span><span>ADOPTED</span><span>SPONSORED</span><span>R.I.P.</span><span>CONTACTS &amp; FORMS</span>
  </nav>

  <!-- hero -->
  <div class="abs hero" role="img" aria-label="Horses grazing in a green paddock with a dog nearby"></div>
  <h1 class="abs hero-title script">Bramblefinch Equine Sanctuary</h1>
  <div class="abs mission">
    <h3>Our Mission</h3>
    <p>We are committed to sustainable and ethical equine rescue and rehabilitation. We believe firmly in improving the physical and psychological well being of every animal that resides at BES, along with actively lobbying and advocating for all companion animals...</p>
  </div>
  <div class="abs btn-white">SHOP NOW</div>
  <div class="abs dot" style="top:505px"></div>
  <div class="abs dot" style="top:530px;background:#f0a81c"></div>
  <div class="abs dot" style="top:555px"></div>

  <!-- about -->
  <div class="abs about-photo" role="img" aria-label="Two ponies greeting each other over a fence"></div>
  <div class="abs about-card">
    <div class="kicker" style="margin-bottom:12px">Equine Sanctuary</div>
    <div class="title-box"><span class="sq"></span><span>Bramblefinch</span></div>
    <p>Bramblefinch Equine Sanctuary (BES) was founded by passionate animal lovers and advocates in 2014, in response to an ever-increasing number of horses passing through the saleyards, and into the hands of knackeries.</p>
    <div class="btn-red" style="width:122px;height:40px;margin-top:18px">READ MORE</div>
  </div>

  <!-- services -->
  <div class="abs services" role="img" aria-label="Faint horse photograph behind an orange wash"></div>
  <div class="abs kicker" style="left:435px;top:1253px;color:#fff">Specialities</div>
  <div class="abs title-box" style="left:435px;top:1284px;width:346px;border-color:#fff;padding-left:4px">
    <span class="sq" style="background:#fff;width:30px;height:54px;opacity:.9"></span><span style="color:#fff">Our Services</span>
  </div>
  <div class="abs service" style="left:150px;background:linear-gradient(#2e3b2a,#4f5a47)" role="img" aria-label="Rider on a horse among trees">HORSES ADOPTION</div>
  <div class="abs service" style="left:466px;background:linear-gradient(#6c7860,#b9b8ad 50%,#515a45)" role="img" aria-label="White pony walking on grass">HORSES SPONSORSHIP</div>
  <div class="abs service" style="left:782px;background:linear-gradient(135deg,#1a1412,#6a3a22 55%,#1d1715)" role="img" aria-label="Bay horse with bridle on dark background">HORSES LEASE</div>
  <div class="abs btn-red" style="left:551px;top:1721px;width:99px;height:39px">VIEW ALL</div>

  <!-- products -->
  <div class="abs kicker" style="left:415px;top:1889px">Shop Now</div>
  <div class="abs title-box" style="left:415px;top:1917px;width:370px">
    <span class="sq"></span><span>Our Products</span>
  </div>
  <div class="abs product" style="left:151px"><div class="img" style="background:linear-gradient(#8a6a4a,#6b7d43)" role="img" aria-label="Candle jars in front of grazing horses"></div><div class="label">CANDLES POURED WITH LOVE (10)</div></div>
  <div class="abs product" style="left:379px"><div class="img" style="background:linear-gradient(#c9c6b8,#7a6a4a 60%,#6f7d3e)" role="img" aria-label="Hay delivered by a farm buggy to horses"></div><div class="label">DONATIONS &nbsp;(6)</div></div>
  <div class="abs product" style="left:608px"><div class="img" style="background:linear-gradient(#cfd8e0,#4f6a3a 60%,#8c8566)" role="img" aria-label="Horses galloping in a field"></div><div class="label">GIFT SHOP (2)</div></div>
  <div class="abs product" style="left:836px"><div class="img" style="background:linear-gradient(#2a2624,#3a302b)" role="img" aria-label="Open day admission ticket with a horse"></div><div class="label">TICKETS OPEN DAY (4)</div></div>

  <!-- get in touch -->
  <div class="abs touch" role="img" aria-label="Volunteer at work behind a red to orange wash"></div>
  <h2 class="abs touch-title">Get In Touch</h2>
  <div class="abs field" style="left:330px;top:2546px;width:260px">Name :</div>
  <div class="abs field" style="left:610px;top:2546px;width:260px">Phone :</div>
  <div class="abs field" style="left:330px;top:2597px;width:260px">Email :</div>
  <div class="abs field" style="left:610px;top:2597px;width:260px">Subject:</div>
  <div class="abs field" style="left:330px;top:2648px;width:540px;height:112px">Message :</div>
  <div class="abs btn-red" style="left:552px;top:2731px;width:116px;height:44px;font-size:14px">SUBMIT</div>

  <div class="abs donate-card">
    <svg class="abs" style="left:18px;top:18px" width="95" height="95" viewBox="0 0 95 95" fill="none" stroke="#e0111f" stroke-width="3">
      <circle cx="55" cy="22" r="17" stroke="#f7923a"/>
      <path d="M55 12v20M60 16h-7a3 3 0 0 0 0 6h4a3 3 0 0 1 0 6h-8" stroke="#f7923a"/>
      <path d="M6 70l14-12c5-4 10-4 16-2l12 4c4 1 4 7-1 7H34m14 0l22-10c5-2 9 3 5 7L45 84 22 82 14 88z"/>
    </svg>
    <div class="info"><b>We are a deductible gift recipient – all donations over $2 are tax deductible.</b><br><b style="font-size:10.5px">Harbour Bank Account:</b> Bramblefinch Equine Sanctuary<br><b style="font-size:10.5px">BSB:</b> 000 142<br><b style="font-size:10.5px">Account:</b> 100234567</div>
  </div>
  <div class="abs donate-big">Donate Now</div>
  <div class="abs card-shape" style="left:824px;background:#1a2a7a"></div>
  <div class="abs card-shape" style="left:877px;background:#2a2a2a"></div>
  <div class="abs card-shape" style="left:930px;background:#e8eef5;border:1px solid #c7d2de"></div>

  <!-- footer -->
  <div class="abs foot-brand"><span class="name">Bramblefinch</span><span class="mark"></span></div>
  <div class="abs foot-nav">HOME<i>|</i>HORSES FOR ADOPTION<i>|</i>FOR SPONSORSHIP<i>|</i>SHOP<i>|</i>LEASE<i>|</i>ADOPTED<i>|</i>SPONSORED<i>|</i>R.I.P<i>|</i>CONTACTS &amp; FORMS</div>

  <div class="abs contact-item" style="left:178px">
    <div class="ring"><svg width="22" height="28" viewBox="0 0 24 30"><path d="M12 1a10 10 0 0 0-10 10c0 8 10 18 10 18s10-10 10-18A10 10 0 0 0 12 1z" fill="#111"/><circle cx="12" cy="11" r="4" fill="#fff"/></svg></div>
    <div class="txt">Bramblefinch Equine<br>Sanctuary Ashvale VIC 3999</div>
  </div>
  <div class="abs contact-item" style="left:480px">
    <div class="ring"><svg width="26" height="20" viewBox="0 0 26 20"><rect x="1" y="1" width="24" height="18" rx="2" fill="#111"/><path d="M2 3l11 8 11-8" stroke="#fff" stroke-width="2" fill="none"/></svg></div>
    <div class="txt"><b>Email</b>admin@bramblefinch.org.au</div>
  </div>
  <div class="abs contact-item" style="left:782px">
    <div class="ring"><svg width="24" height="24" viewBox="0 0 24 24"><path d="M6.6 10.8a15 15 0 0 0 6.6 6.6l2.2-2.2c.3-.3.7-.4 1-.2 1.1.4 2.3.6 3.6.6.6 0 1 .4 1 1V20c0 .6-.4 1-1 1A17 17 0 0 1 3 4c0-.6.4-1 1-1h3.5c.6 0 1 .4 1 1 0 1.3.2 2.5.6 3.6.1.3 0 .7-.2 1z" fill="#111"/></svg></div>
    <div class="txt"><b>Phone</b>0400 555 101 or 0400 555 202</div>
  </div>

  <div class="abs rule" style="left:193px;width:195px"></div>
  <div class="abs rule" style="left:812px;width:195px"></div>
  <div class="abs copyright">© 2022 Bramblefinch Equine Sanctuary. All Rights Reserved</div>
  <div class="abs to-top"><svg width="14" height="14" viewBox="0 0 14 14" fill="none" stroke="#fff" stroke-width="2"><path d="M2 7l5-5 5 5M2 12l5-5 5 5"/></svg></div>
</div>
</body>
</html>
```